Harbour Vale Lettings Web Site Design

I am after a very simple 3 page web site please. I attach a PDF with the text and information. The logo is also in the PDF. The colours should be orange and blues. The pages should be HOME - LANDLORDS - TENANTS.
Lettings and Property Management Company aimed at just being a reference point for tenants but more of a sales pitch to landlords. Please refer to the attached PDF and word file which contains far more content for the various pages.

Target Market(s)

Prospective Landlords mainly but tenants also

Industry/Entity Type

Lettings and Property Management

Number of Pages Required

3 page

Font styles to use
Sans Serif
Other font styles liked:
• Candara

Colors
0054AA
0677BA
7BADD7
CADEEF
E8F1F8
F0912C
F2A743
F7CA91
FBE8D2
FDF5EE

Requirements
Must have
• Must be colour co-ordinated to the logo (orange and dark blue predominently, Must have good quality stock images relating to property and renting out property. Should have home page and links to landlord page and tenant page. Must have the 4 logos that we are affiliated to (TKR, Tenancy Settle, BNF and Funds Guard Scheme) - all attached.
Nice to have
• Modern feel, crisp and sharp but simple - good stock images.

```html
<!DOCTYPE html>
<html lang="en">
<head>
<meta charset="utf-8">
<title>Harbour Vale Lettings – Home</title>
<link href="https://fonts.googleapis.com/css2?family=Tinos:wght@400;700&family=Figtree:wght@400;500;700&display=swap" rel="stylesheet">
<style>
:root{
  --navy:#27355f;
  --navy-deep:#1f2b52;
  --orange:#e8891e;
  --orange-soft:#e6a24f;
  --sky:#4aa9cc;
  --sky-light:#e6f2f8;
  --ink:#1b1b1b;
  --paper:#ffffff;
  --mist:#f5f5f5;
  --line:#d4e2f0;
}
*{box-sizing:border-box;margin:0;padding:0}
html,body{width:750px;height:1200px;overflow:hidden}
body{position:relative;background:var(--paper);font-family:'Figtree',sans-serif;color:var(--ink)}
a{text-decoration:none}

/* hero */
.hero{position:absolute;left:0;top:0;width:750px;height:318px;overflow:hidden;
  background:linear-gradient(180deg,#3a466f 0%,#45527e 50%,#56628c 100%)}
.hero-photo{position:absolute;inset:0;
  background:
    radial-gradient(ellipse 190px 90px at 230px 110px,rgba(205,175,170,.38),transparent 70%),
    radial-gradient(ellipse 160px 70px at 470px 150px,rgba(190,165,165,.3),transparent 70%),
    radial-gradient(ellipse 170px 95px at 210px 270px,rgba(215,215,225,.42),transparent 70%),
    radial-gradient(ellipse 140px 110px at 590px 250px,rgba(220,220,230,.38),transparent 70%),
    radial-gradient(ellipse 110px 60px at 60px 230px,rgba(150,160,190,.3),transparent 70%),
    linear-gradient(90deg,rgba(30,40,75,.35) 0%,transparent 25%,transparent 75%,rgba(30,40,75,.35) 100%)}
.contact{position:absolute;display:flex;align-items:center;gap:8px;color:#fff}
.contact-icon{width:31px;height:31px;flex:none}
.contact strong{display:block;font-family:'Tinos',serif;font-size:10px;font-weight:700}
.contact span{display:block;font-size:7.5px}
.hero .contact{left:89px;top:9px}
.nav{position:absolute;top:20px;right:165px;display:flex;gap:18px;font-family:'Tinos',serif;font-weight:700;font-size:10px;letter-spacing:.3px}
.nav a{color:#fff}
.nav a.active{color:var(--orange)}
.brand{position:absolute;left:0;width:750px;text-align:center;color:#fff;font-family:'Tinos',serif;font-weight:400}
.brand-mark{position:absolute;left:350px;top:66px;width:50px;height:50px;border-radius:50%;background:var(--orange)}
.hero .brand{top:150px;font-size:29px;line-height:29px;letter-spacing:2px}
.tagline{position:absolute;top:234px;left:0;width:750px;text-align:center;color:#fff;font-family:'Tinos',serif;font-weight:400;font-size:30px}

/* features */
.features{position:absolute;top:361px;left:90px;display:flex;gap:8px}
.feature{width:186px;height:108px;border:1px solid var(--line);border-radius:3px;background:#fff;
  box-shadow:0 2px 4px rgba(40,60,100,.06);padding:17px 0 0 12px}
.feature-icon{width:46px;height:32px;display:block}
.feature h3{font-family:'Tinos',serif;font-weight:400;font-size:14px;color:var(--navy);margin-top:9px}
.feature p{font-size:8.5px;margin-top:3px}

/* about */
.section-title{position:absolute;left:0;width:750px;text-align:center;font-family:'Tinos',serif;font-weight:400;color:var(--navy)}
.rule{position:absolute;height:2px;width:45px;background:var(--sky)}
.about-title{top:512px;font-size:23px}
.about-intro{position:absolute;top:558px;left:94px;width:562px;text-align:center;font-size:8.4px;line-height:16px}
.about-intro b{font-weight:700;font-size:9px}
.about-visual{position:absolute;left:104px;top:618px;width:228px;height:170px;border-radius:26px;
  background:
    radial-gradient(ellipse 70px 55px at 140px 80px,rgba(60,70,110,.85),transparent 75%),
    radial-gradient(ellipse 90px 45px at 130px 150px,rgba(90,175,210,.9),transparent 75%),
    linear-gradient(115deg,#e9a24c 0%,#e2a560 38%,#5a6590 62%,#5aaed0 100%)}
.about-copy{position:absolute;left:374px;top:629px;width:295px;font-size:8.4px;line-height:16px}
.about-copy p+p{margin-top:3px}
.cta{position:absolute;left:373px;top:737px;width:178px;height:38px;background:var(--sky);color:#fff;text-align:center;padding-top:6px}
.cta strong{display:block;font-size:11px;font-weight:700}
.cta span{display:block;font-size:8px;margin-top:1px}

/* affiliations */
.affiliations{position:absolute;top:820px;left:0;width:750px;height:300px;background:var(--mist)}
.aff-title{top:878px;font-size:23px}
.aff-title em{font-style:normal;color:var(--orange)}
.badges{position:absolute;top:922px;left:93px;display:flex;gap:6px}
.badge{width:140px;height:81px;background:#fff;border:1px solid #e3e8ef;box-shadow:0 1px 3px rgba(0,0,0,.06);display:flex;align-items:center;justify-content:center}
.badge-shape{display:block}

/* footer */
.footer-band{position:absolute;left:0;top:1050px;width:750px;height:150px}
.footer .contact{top:1115px}
.footer .brand{top:1122px;font-size:12px;line-height:13px;letter-spacing:1px}
.footer-mark{position:absolute;left:362px;top:1088px;width:26px;height:26px;border-radius:50%;background:var(--orange)}
.footer-rule{position:absolute;left:91px;top:1167px;width:577px;height:1px;background:rgba(255,255,255,.2)}
.copyright{position:absolute;top:1176px;left:0;width:750px;text-align:center;color:#fff;font-size:8px}
</style>
</head>
<body>

<header class="hero">
  <div class="hero-photo" role="img" aria-label="Photo of a hand passing house keys above small model houses, tinted navy"></div>
  <div class="contact">
    <svg class="contact-icon" viewBox="0 0 31 31"><circle cx="15.5" cy="15.5" r="13" fill="none" stroke="#fff" stroke-opacity=".35" stroke-width="3"/><rect x="9.5" y="11" width="12" height="9" fill="none" stroke="#fff"/><path d="M9.5 11l6 5 6-5" fill="none" stroke="#fff"/></svg>
    <div><strong>Email Us</strong><span>enquiries@harbourvalelettings.com</span></div>
  </div>
  <nav class="nav"><a class="active" href="#">HOME</a><a href="#">LANDLORDS</a><a href="#">TENANTS</a></nav>
  <div class="brand-mark"></div>
  <div class="brand">HARBOUR VALE<br>LETTINGS</div>
  <h1 class="tagline">Let Us Manage Your Property</h1>
</header>

<section class="features">
  <article class="feature">
    <svg class="feature-icon" viewBox="0 0 46 32"><circle cx="14" cy="15" r="14" fill="var(--sky-light)"/><circle cx="18" cy="6" r="2.5" fill="none" stroke="var(--orange)" stroke-width="1.2"/><path d="M18 8.5v8" stroke="var(--orange)" stroke-width="1.2"/><path d="M24 11l7-6 7 6v8H24z" fill="none" stroke="var(--orange)" stroke-width="1.2"/><rect x="29" y="14" width="4" height="5" fill="none" stroke="var(--orange)"/><path d="M15 22h3v7h-3zM18 24h10l6-2-2 5H18" fill="none" stroke="var(--sky)" stroke-width="1.2"/></svg>
    <h3>Fully Managed Lettings</h3><p>We handle everything</p>
  </article>
  <article class="feature">
    <svg class="feature-icon" viewBox="0 0 46 32"><circle cx="14" cy="15" r="14" fill="var(--sky-light)"/><path d="M18 9l7-7 7 7v11H18z" fill="none" stroke="var(--orange)" stroke-width="1.2"/><circle cx="25" cy="10" r="2" fill="none" stroke="var(--orange)"/><path d="M25 12v6" stroke="var(--orange)" stroke-width="1.2"/><path d="M14 22h3v7h-3zM17 24h8l6-4-2 6-12 2" fill="none" stroke="var(--sky)" stroke-width="1.2"/></svg>
    <h3>Quick Landlord Onboarding</h3><p>Hassle-free onboarding</p>
  </article>
  <article class="feature">
    <svg class="feature-icon" viewBox="0 0 46 32"><circle cx="14" cy="15" r="14" fill="var(--sky-light)"/><circle cx="20" cy="5" r="3" fill="none" stroke="var(--orange)" stroke-width="1.2"/><path d="M23 5h13v3M32 5v3" fill="none" stroke="var(--orange)" stroke-width="1.2"/><path d="M13 19l7-6 5 3 6-4 6 7-9 9-6-4z" fill="none" stroke="var(--sky)" stroke-width="1.2"/><path d="M20 20l5 4M23 18l5 4" stroke="var(--sky)" stroke-width="1"/></svg>
    <h3>Reliable Tenant Support</h3><p>Always ready to help</p>
  </article>
</section>

<h2 class="section-title about-title">ABOUT US</h2>
<div class="rule" style="left:353px;top:542px"></div>
<p class="about-intro"><b>Harbour Vale Lettings</b> has emerged after over 20 years of privately managing our own rental properties. We are family run and decided to move all of our properties under one ‘umbrella’. Now professionally set up as a legal entity, Harbour Vale is looking to welcome new tenants and landlords to an innovative and fresh way of letting property.</p>
<div class="about-visual" role="img" aria-label="Photo of smiling letting agents greeting a couple, in warm orange and blue tones"></div>
<div class="about-copy">
  <p>We always maintain a high standard of service and our friendly and helpful team are experienced in all areas and offer an excellent service in helping landlords and tenants deal with problems and issues they face daily.</p>
  <p>Out of hours emergency service which means we are there (in an emergency) for our tenants and landlords 24/7.</p>
</div>
<a class="cta" href="#"><strong>LANDLORD ENQUIRY</strong><span>Actively Looking for new landlords</span></a>

<section class="affiliations"></section>
<h2 class="section-title aff-title">WE ARE MEMBERS OF <em>or</em> AFFILIATED TO</h2>
<div class="rule" style="left:355px;top:909px"></div>
<div class="badges">
  <div class="badge"><svg class="badge-shape" width="56" height="60" role="img" aria-label="TKR membership badge"><rect width="56" height="60" rx="5" fill="#7dc143"/></svg></div>
  <div class="badge"><svg class="badge-shape" width="124" height="34" role="img" aria-label="Funds Guard Scheme membership badge"><rect width="124" height="34" rx="4" fill="#6ccf8f"/></svg></div>
  <div class="badge"><svg class="badge-shape" width="122" height="34" role="img" aria-label="Tenancy Settle membership badge"><rect width="122" height="34" rx="4" fill="#8a3c8f"/></svg></div>
  <div class="badge"><svg class="badge-shape" width="78" height="59" role="img" aria-label="BNF registration badge"><rect width="78" height="59" fill="#112a5c"/></svg></div>
</div>

<footer class="footer">
  <svg class="footer-band" viewBox="0 0 750 150"><polygon points="0,53 375,3 750,53 750,150 0,150" fill="var(--orange)"/><polygon points="0,61 375,11 750,61 750,150 0,150" fill="var(--navy)"/></svg>
  <div class="footer-mark"></div>
  <div class="brand">HARBOUR VALE<br>LETTINGS</div>
  <div class="contact" style="left:89px">
    <svg class="contact-icon" viewBox="0 0 31 31"><circle cx="15.5" cy="15.5" r="13" fill="none" stroke="#fff" stroke-opacity=".35" stroke-width="3"/><path d="M15.5 22s-5-5-5-9a5 5 0 0110 0c0 4-5 9-5 9z" fill="none" stroke="#fff"/><circle cx="15.5" cy="13" r="1.8" fill="none" stroke="#fff"/></svg>
    <div><strong>Harbour Vale Letting Property Mgmt.</strong><span>48 Quayside Row, Portlen PL 20418</span></div>
  </div>
  <div class="contact" style="left:507px">
    <svg class="contact-icon" viewBox="0 0 31 31"><circle cx="15.5" cy="15.5" r="13" fill="none" stroke="#fff" stroke-opacity=".35" stroke-width="3"/><rect x="9.5" y="11" width="12" height="9" fill="none" stroke="#fff"/><path d="M9.5 11l6 5 6-5" fill="none" stroke="#fff"/></svg>
    <div><strong>Email Us</strong><span>enquiries@harbourvalelettings.com</span></div>
  </div>
  <div class="footer-rule"></div>
  <p class="copyright">© 2025 Harbour Vale Letting Property Management. All Rights Reserved.</p>
</footer>

</body>
</html>
```